Business card for real estate agent / office

We're looking for a new business card. We want something that is pretty clean, modern and sleek. Something that also tells people that we are a new age company...cutting edge. Although real estate has been done a certain way the last 100 years, we have energy and vibrance. Company name is Silver Meadow Properties. info can be found here: http://www.smprealtyhub.example/

needs to include: Name, title, phone number, email. our license number also needs to be displayed somewhere.

Target Market(s)

25-55 homeowners or potential homeowners

Industry/Entity Type

Business

Contact Information for Business Card

we need business card designs for real estate agent / office

Font styles to use
Serif

Requirements
Must have
• needs to include: Name, title, phone number, email. our license number also needs to be displayed somewhere and company name.
Nice to have
• placement area for photo

```html
<!DOCTYPE html>
<html lang="en">
<head>
<meta charset="utf-8">
<title>Silver Meadow Properties – Business Card</title>
<link rel="stylesheet" href="https://fonts.googleapis.com/css2?family=Lora:wght@400;600;700&display=swap">
<style>
  :root {
    --backdrop: #9c9c9c;
    --paper: #f3f3f2;
    --navy: #143f69;
    --navy-soft: #5f83a6;
    --green: #4caf3a;
    --white: #ffffff;
    --muted-white: #d7e1ec;
  }
  * { box-sizing: border-box; margin: 0; padding: 0; }
  html, body {
    width: 1200px;
    height: 1200px;
    overflow: hidden;
    background: var(--backdrop);
    font-family: "Lora", serif;
  }
  .canvas {
    position: relative;
    width: 1200px;
    height: 1200px;
  }
  .card {
    position: absolute;
    left: 236px;
    width: 724px;
    height: 412px;
    overflow: hidden;
  }
  /* Front */
  .card-front { top: 148px; background: var(--paper); }
  .portrait {
    position: absolute;
    left: 287px;
    top: 24px;
    width: 150px;
    height: 150px;
    border-radius: 50%;
    background: radial-gradient(circle at 50% 70%, var(--navy-soft) 0%, var(--navy) 68%);
  }
  .agent-name {
    position: absolute;
    top: 190px;
    width: 100%;
    text-align: center;
    color: var(--navy);
    font-size: 35px;
    font-weight: 700;
    line-height: 1.2;
  }
  .agent-title {
    position: absolute;
    top: 238px;
    width: 100%;
    text-align: center;
    color: var(--navy);
    font-size: 18px;
    font-weight: 400;
    line-height: 1.2;
  }
  .contact-band {
    position: absolute;
    left: 0;
    top: 290px;
    width: 100%;
    height: 122px;
    background: var(--navy);
    border-top: 6px solid var(--green);
  }
  .contact-item {
    position: absolute;
    top: 22px;
    width: 260px;
    margin-left: -130px;
    text-align: center;
    color: var(--white);
    font-size: 17px;
    font-weight: 400;
    line-height: 1.2;
    white-space: nowrap;
  }
  .contact-item svg { display: block; margin: 0 auto 14px; }
  .contact-web { left: 140px; }
  .contact-phone { left: 362px; }
  .contact-mail { left: 588px; }
  /* Back */
  .card-back { top: 634px; background: var(--navy); }
  .brand-seal {
    position: absolute;
    left: 228px;
    top: 72px;
    width: 268px;
    height: 268px;
    border-radius: 50%;
    background: var(--white);
    border: 12px solid var(--green);
    display: flex;
    align-items: center;
    justify-content: center;
    text-align: center;
  }
  .brand-name {
    color: var(--navy);
    font-size: 27px;
    font-weight: 700;
    line-height: 1.2;
  }
  .license-number {
    position: absolute;
    top: 366px;
    width: 100%;
    text-align: center;
    color: var(--muted-white);
    font-size: 15px;
    font-weight: 400;
    letter-spacing: 1px;
  }
</style>
</head>
<body>
<main class="canvas">
  <section class="card card-front">
    <div class="portrait" role="img" aria-label="Agent portrait photo"></div>
    <h1 class="agent-name">Daniel Okafor</h1>
    <p class="agent-title">Real Estate Broker, Realtor, MBA</p>
    <div class="contact-band">
      <div class="contact-item contact-web">
        <svg width="38" height="38" viewBox="0 0 38 38" aria-hidden="true">
          <circle cx="19" cy="19" r="19" fill="var(--white)"/>
          <g fill="none" stroke="var(--navy)" stroke-width="1.6">
            <circle cx="19" cy="19" r="11"/>
            <ellipse cx="19" cy="19" rx="5" ry="11"/>
            <line x1="8" y1="19" x2="30" y2="19"/>
            <line x1="19" y1="8" x2="19" y2="30"/>
            <path d="M10 13.5h18M10 24.5h18"/>
          </g>
        </svg>
        www.smprealtyhub.example
      </div>
      <div class="contact-item contact-phone">
        <svg width="38" height="38" viewBox="0 0 38 38" aria-hidden="true">
          <circle cx="19" cy="19" r="19" fill="var(--white)"/>
          <g fill="var(--navy)">
            <path d="M8 15c0-3 5-5 11-5s11 2 11 5v2h-6v-3h-10v3H8z"/>
            <path d="M13 18h12l3 10H10z"/>
          </g>
          <circle cx="19" cy="23" r="2.6" fill="var(--white)"/>
        </svg>
        555.014.7291
      </div>
      <div class="contact-item contact-mail">
        <svg width="38" height="38" viewBox="0 0 38 38" aria-hidden="true">
          <circle cx="19" cy="19" r="19" fill="var(--white)"/>
          <rect x="9" y="12" width="20" height="14" fill="none" stroke="var(--navy)" stroke-width="1.8"/>
          <path d="M9 12l10 8 10-8" fill="none" stroke="var(--navy)" stroke-width="1.8"/>
        </svg>
        dan@smprealtyhub.example
      </div>
    </div>
  </section>

  <section class="card card-back">
    <div class="brand-seal">
      <p class="brand-name">Silver Meadow<br>Properties</p>
    </div>
    <p class="license-number">LICENSE #02081457</p>
  </section>
</main>
</body>
</html>
```